Corvell Law, PC Letterhead Design -- LAW FIRM

I am looking for a very elegant letterhead design for my personal injury law practice.
The letter head must have 4 different variations of the same thing meaning one design that has just a header, and another with a header and footer.
Elegance is key, I do not want it to be too bold. Please stay away from colors that are not black, white or gray or silver.
Please include a gradient style letterhead for the header while implementing the design of the logo found in folder #3
I have attached for you the logos and emblems for my company below.
In folders 1-4 you will find my actual logo.
In folder 5-6 you will find a shorter version of my logo, this can be implemented maybe in the footer + header design of the letter head (do not include this shortened version in the header).
In folders 7-8 you will find an emblem for my company.
Information that needs to be found on the letterhead is as follows:
A clearly written version of my company name: Corvell Law, PC
Address: 4718 Tamsden Avenue Suite #512, Beverly Hills, CA, 90210
Email: desmond@corvelllaw-example.com
Telephone number: 310-555-0147

```html
<!DOCTYPE html>
<html lang="en">
<head>
<meta charset="utf-8">
<title>Corvell Law, PC — Letterhead</title>
<link rel="stylesheet" href="https://fonts.googleapis.com/css2?family=Barlow:wght@400&family=Carlito&family=Poppins:wght@400&display=swap">
<style>
  :root {
    --backdrop: #3a3a3a;
    --paper: #ffffff;
    --ink: #1a1a1a;
    --ink-soft: #2b2b2b;
    --watermark: #ececec;
    --band: #d3d4d6;
    --signature-tone: #e4e4e4;
  }
  * { margin: 0; padding: 0; box-sizing: border-box; }
  html, body { width: 1200px; height: 1200px; overflow: hidden; }
  body { background: var(--backdrop); position: relative; }
  .sheet {
    position: absolute;
    top: 215px;
    width: 545px;
    height: 769px;
    background: var(--paper);
    color: var(--ink);
    overflow: hidden;
  }
  .sheet--header-only { left: 43px; font-family: "Barlow", sans-serif; letter-spacing: 0.25px; }
  .sheet--header-footer { left: 608px; font-family: "Carlito", sans-serif; }

  .firm-name {
    position: absolute;
    font-size: 26px;
    font-weight: 400;
    letter-spacing: 0.5px;
    color: var(--ink);
    white-space: nowrap;
  }
  .sheet--header-only .firm-name { top: 62px; left: 0; width: 100%; text-align: center; }
  .sheet--header-footer .firm-name { top: 72px; left: 52px; }

  .contact {
    position: absolute;
    right: 38px;
    top: 76px;
    font-family: "Poppins", sans-serif;
    font-size: 9px;
    line-height: 14px;
    color: var(--ink-soft);
  }
  .contact-line { display: flex; align-items: center; gap: 4px; white-space: nowrap; }
  .contact-line svg { width: 7px; height: 7px; flex: none; }

  .watermark {
    position: absolute;
    left: 142px;
    top: 255px;
    width: 260px;
    height: 260px;
    border-radius: 50%;
    background: var(--watermark);
  }

  .recipient, .salutation, .body-copy, .closing { position: absolute; left: 51px; }
  .sheet--header-only .recipient { top: 176px; font-size: 11px; line-height: 13.2px; }
  .sheet--header-only .salutation { top: 266px; font-size: 11px; }
  .sheet--header-only .body-copy { top: 298px; width: 445px; font-size: 11px; line-height: 16.5px; }
  .sheet--header-only .signature { left: 50px; top: 583px; width: 93px; height: 50px; }
  .sheet--header-only .closing { top: 636px; font-size: 11px; }
  .footer-rule {
    position: absolute;
    left: 52px;
    top: 735px;
    width: 432px;
    height: 1px;
    background: var(--ink);
  }

  .sheet--header-footer .recipient { top: 187px; font-size: 10.3px; line-height: 13.2px; }
  .sheet--header-footer .salutation { top: 281px; font-size: 10.3px; }
  .sheet--header-footer .body-copy { top: 313px; width: 440px; font-size: 10.3px; line-height: 16.5px; }
  .sheet--header-footer .closing { top: 537px; font-size: 10.3px; }
  .sheet--header-footer .signature { left: 46px; top: 561px; width: 181px; height: 36px; }

  .signature { position: absolute; background: var(--signature-tone); border-radius: 3px; }

  .footer-band {
    position: absolute;
    left: 0;
    top: 736px;
    width: 100%;
    height: 15px;
    background: var(--band);
  }
  .footer-address {
    position: absolute;
    top: 736px;
    left: 0;
    width: 542px;
    height: 15px;
    line-height: 15px;
    text-align: center;
    font-family: "Poppins", sans-serif;
    font-size: 9.5px;
    color: var(--ink);
    white-space: nowrap;
  }
  .footer-mark {
    position: absolute;
    left: 466px;
    top: 723px;
    width: 34px;
    height: 34px;
    border-radius: 50%;
    background: #c4c5c8;
    border: 1px solid #ffffff;
  }
</style>
</head>
<body>

<section class="sheet sheet--header-only">
  <div class="watermark"></div>
  <div class="firm-name">Corvell Law, PC</div>
  <address class="recipient" style="font-style:normal">
    Mr. John Doe<br>President<br>Meridian Accountants<br>111 Street Name,<br>City State, 12345
  </address>
  <p class="salutation">Dear :</p>
  <div class="body-copy">
    <p>Lorem ipsum dolor sit amet, consectetur adipiscing elit. Aenean ut ipsum eget massa hendrerit vestibulum vel in velit. Donec pretium neque velit.</p>
    <p>Aliquam porta lectus nec mauris ornare venenatis. Vivamus non est turpis, et cursus sem. Mauris vehicula erat in diam auctor at bibendum nisl lacinia.</p>
    <p>Morbi imperdiet neque vehicula nunc convallis gravida. Vestibulum iaculis pretium placerat. Integer consequat, est sit amet facilisis eleifend, nibh nibh varius orci, eget dapibus arcu dui non purus. Pellentesque in magna mauris. Duis enim sapien, dictum vitae condimentum a, pulvinar vel lacus. Mauris et molestie nibh. Vestibulum vitae nulla at metus elementum porta sit amet interdum elit. Nulla sollicitudin neque eu nulla volutpat congue.</p>
    <p>Etiam pellentesque, velit id dapibus fermentum, turpis sapien ornare dui, ac tincidunt ligula odio congue purus. Nunc sed ante dui, in porta lectus. Cras nec sem lorem. In hac habitasse platea dictumst. Maecenas id diam quis dui porta tristique. Sed id egestas felis. Donec ullamcorper mattis posuere. Phasellus fermentum eleifend tortor vel dapibus. Vestibulum ante ipsum.</p>
  </div>
  <div class="signature" role="img" aria-label="Handwritten signature"></div>
  <p class="closing">Sincerely,</p>
  <div class="footer-rule"></div>
</section>

<section class="sheet sheet--header-footer">
  <div class="firm-name">Corvell Law, PC</div>
  <div class="contact">
    <div class="contact-line">
      <svg viewBox="0 0 10 10"><rect x="0.5" y="1.5" width="9" height="7" fill="none" stroke="#1a1a1a" stroke-width="1.2"/><path d="M0.5 1.5 L5 5.5 L9.5 1.5" fill="none" stroke="#1a1a1a" stroke-width="1.2"/></svg>
      desmond@corvelllaw-example.com
    </div>
    <div class="contact-line">
      <svg viewBox="0 0 10 10"><path d="M2 0.8 L3.8 3 L2.8 4.2 Q4 6.4 5.8 7.2 L7 6.2 L9.2 8 L8 9.4 Q3.5 9 0.6 2 Z" fill="#1a1a1a"/></svg>
      310-555-0147
    </div>
  </div>
  <address class="recipient" style="font-style:normal">
    Mr. John Doe<br>President<br>Meridian Accountants<br>111 Street Name,<br>City State, 12345
  </address>
  <p class="salutation">Dear :</p>
  <div class="body-copy">
    <p>Lorem ipsum dolor sit amet, consectetur adipiscing elit. Aenean ut ipsum eget massa hendrerit vestibulum vel in velit. Donec pretium neque velit.</p>
    <p>Aliquam porta lectus nec mauris ornare venenatis. Vivamus non est turpis, et cursus sem. Mauris vehicula erat in diam auctor at bibendum nisl lacinia.</p>
    <p>Morbi imperdiet neque vehicula nunc convallis gravida. Vestibulum iaculis pretium placerat. Integer consequat, est sit amet facilisis eleifend, nibh nibh varius orci, eget dapibus arcu dui non purus. Pellentesque in magna mauris. Duis enim sapien, dictum vitae condimentum a, pulvinar vel lacus. Mauris et molestie nibh. Vestibulum vitae nulla at metus elementum porta sit amet interdum elit. Nulla sollicitudin neque eu nulla volutpat congue.</p>
    <p>Etiam pellentesque, velit id dapibus fermentum, turpis sapien ornare dui, ac tincidunt ligula odio congue purus. Nunc sed ante dui, in porta lectus. Cras nec sem lorem. In hac habitasse platea dictumst. Maecenas id diam quis dui porta tristique. Sed id egestas felis. Donec ullamcorper mattis posuere. Phasellus fermentum eleifend tortor vel dapibus. Vestibulum ante ipsum.</p>
  </div>
  <p class="closing">Sincerely,</p>
  <div class="signature" role="img" aria-label="Script signature of Elliot Varga"></div>
  <div class="footer-band"></div>
  <p class="footer-address">4718 Tamsden Avenue Suite #512, Beverly Hills, CA, 90210</p>
  <div class="footer-mark"></div>
</section>

</body>
</html>
```